Harbison Projects Promo Brochure

Design a simple ,visually impactful brochure that will articulate our company experience and services to prospective clients.

We need to project to have the following elements / structure:
1. Company Intro
2. Company Services
3. Experience
4. Contact Info
5. Images

I'd like to use icons and imagery as needed to illustrate services and experience.
This brochure will be emailed, so the final version will need to be compressed.

I've uploaded our Owner Rep Services, which has phasing, and services (within each phase), see attached. This info needs to be cleanly added to a brochure.

The "Why Harbison Building Management" doc, copy, needs to be included in the brochure.

Include contact info:
Harbison Projects Services, LLC
214-555-0193
www.harbisonprojgroup.example

Target Market(s)

Restaurants and Hospitality Concepts

Font styles to use
Sans Serif

Colors

Designer to choose colors to be used in the design.

Requirements
Must have
• Very easy to read. Clean.
Information and images should be balanced nicely on the page.

use colors of our logo: red, black, grey, white
Should not have
• Very busy text or images.

```html
<!DOCTYPE html>
<html lang="en">
<head>
<meta charset="utf-8">
<title>Harbison Projects Brochure</title>
<link href="https://fonts.googleapis.com/css2?family=Poppins:wght@400;500;600;700;800&display=swap" rel="stylesheet">
<style>
:root{
  --red:#e5261f;
  --black:#161616;
  --ink:#2a2a2a;
  --grey:#e6e6e6;
  --stage:#c9c9c9;
  --white:#ffffff;
}
*{margin:0;padding:0;box-sizing:border-box}
html,body{width:949px;height:1200px;overflow:hidden}
body{background:var(--stage);font-family:"Poppins",sans-serif;position:relative;color:var(--ink)}
.page{position:absolute;top:309px;width:530px;height:685px;background:var(--white);overflow:hidden;transform:scale(.85);transform-origin:0 0;box-shadow:0 2px 8px rgba(0,0,0,.2)}
.page--front{left:16px}
.page--back{left:483px}
.page-art{position:absolute;inset:0}
.abs{position:absolute}

/* front page: intro column */
.intro{left:6px;top:22px;width:196px;text-align:center;color:var(--white)}
.brand-mark{display:flex;flex-direction:column;align-items:center;gap:6px}
.brand-mark .square{width:40px;height:40px;background:var(--red)}
.brand-mark .name{font-size:7px;font-weight:700;letter-spacing:.3px;text-transform:uppercase}
.headline{margin-top:14px}
.headline .big{font-size:31px;font-weight:800;color:var(--red);line-height:1}
.headline .mid{font-size:21px;font-weight:700;line-height:1.1}
.headline .bar{display:inline-block;background:var(--red);font-size:13px;font-weight:700;padding:1px 8px;margin-top:2px;text-transform:uppercase}
.headline .small{font-size:13px;font-weight:700;margin-top:2px}
.intro .note{font-size:7px;line-height:1.25;margin-top:4px}
.intro .label{font-size:8px;font-weight:700;margin-top:14px;padding-bottom:3px;border-bottom:1px solid var(--red);margin-left:20px;margin-right:20px}
.intro p{font-size:8px;line-height:1.3;margin-top:6px;padding:0 8px}
.intro p b{font-weight:700}
.intro .network{font-weight:700;font-size:7.5px}
.offer-list{list-style:none;margin-top:20px}
.offer-list li{font-size:11px;font-weight:600;text-transform:uppercase}
.offer-list .plus{display:block;width:11px;height:11px;border-radius:50%;background:var(--red);margin:8px auto;position:relative}
.offer-list .plus::before,.offer-list .plus::after{content:"";position:absolute;background:var(--white);left:50%;top:50%;transform:translate(-50%,-50%)}
.offer-list .plus::before{width:6px;height:1.5px}
.offer-list .plus::after{width:1.5px;height:6px}

/* services */
.services{right:18px;top:388px;width:175px;text-align:right}
.services h2{font-size:12px;font-weight:700;color:var(--black);padding-bottom:3px;border-bottom:1px solid var(--red)}
.services ul{list-style:none;margin-top:8px}
.services li{font-size:11px;line-height:1.3;margin-bottom:9px;display:flex;justify-content:flex-end;align-items:flex-start;gap:6px}
.services li .dot{flex:none;width:11px;height:11px;border-radius:50%;background:var(--black);border:2px solid var(--red);margin-top:2px}

/* contact */
.contact{color:var(--white);text-align:center}
.contact .lead{font-size:12px}
.contact .phone{font-size:24px;font-weight:700;line-height:1.1;display:flex;align-items:center;justify-content:center;gap:8px}
.contact .phone svg{width:18px;height:18px}
.contact .web{font-size:12px;font-weight:700}
.contact .web span{color:var(--red)}
.page--front .contact{left:160px;top:607px;width:220px}
.corner-name{right:14px;bottom:24px;display:flex;align-items:center;gap:6px;color:var(--white);font-size:10px;font-weight:700;text-transform:uppercase}
.corner-name .square{width:14px;height:14px;background:var(--red)}

/* back page */
.why{left:0;top:16px;width:530px;text-align:center}
.why h1{font-size:15px;font-weight:700;color:var(--white)}
.why .simple{font-size:24px;font-weight:800;color:var(--red);line-height:1.1}
.reasons{top:112px;width:238px}
.reasons--left{left:18px}
.reasons--right{left:281px;width:232px}
.reason{margin-bottom:16px}
.reason h3{display:flex;align-items:center;gap:6px;font-size:11px;font-weight:700;color:var(--red);text-transform:uppercase}
.reason h3 .dot{width:12px;height:12px;border-radius:50%;background:var(--black);border:2px solid var(--red)}
.reason p{font-size:7.6px;line-height:1.3;margin-left:26px;margin-top:1px;color:#333}
.reason p b{color:var(--red);font-weight:600}
.reason p strong{font-weight:600;color:var(--black)}
.divider{left:264px;top:112px;width:1px;height:360px;background:var(--grey)}
.back-name{left:0;width:530px;top:520px;display:flex;flex-direction:column;align-items:center;gap:5px;color:var(--white);font-size:7px;font-weight:700;text-transform:uppercase}
.back-name .square{width:34px;height:34px;background:var(--red)}
.page--back .contact{left:140px;top:604px;width:250px}
</style>
</head>
<body>

<section class="page page--front">
  <svg class="page-art" viewBox="0 0 530 685" aria-hidden="false">
    <polygon points="0,0 292,0 292,470 0,665" fill="#161616"/>
    <polygon points="0,665 292,470 380,415 392,428 0,685" fill="#e5261f"/>
    <polygon points="190,597 530,597 530,685 60,685" fill="#161616"/>
    <polygon points="150,625 190,597 220,597 175,625" fill="#e5261f"/>
    <polygon points="360,-25 533,75 533,275 360,375 187,275 187,75" fill="#e5261f"/>
    <polygon points="360,-10 520,82 520,268 360,360 200,268 200,82" fill="#ffffff"/>
    <g role="img" aria-label="Aerial evening view of a lit outdoor restaurant and entertainment venue">
      <defs>
        <linearGradient id="venue" x1="0" y1="0" x2="0" y2="1">
          <stop offset="0" stop-color="#6e6a8c"/>
          <stop offset=".45" stop-color="#3f5a3a"/>
          <stop offset="1" stop-color="#223024"/>
        </linearGradient>
        <linearGradient id="storefront" x1="0" y1="0" x2="0" y2="1">
          <stop offset="0" stop-color="#3a3d52"/>
          <stop offset=".55" stop-color="#7a1d1a"/>
          <stop offset="1" stop-color="#3f7a2c"/>
        </linearGradient>
      </defs>
      <polygon points="360,-3 514,86 514,264 360,353 206,264 206,86" fill="url(#venue)"/>
    </g>
    <polygon points="268,272 335.5,311 335.5,389 268,428 200.5,389 200.5,311" fill="#e5261f"/>
    <g role="img" aria-label="Restaurant storefront at dusk with lawn in front">
      <polygon points="268,282 327,316 327,384 268,418 209,384 209,316" fill="url(#storefront)"/>
    </g>
  </svg>

  <div class="abs intro">
    <div class="brand-mark"><span class="square"></span><span class="name">Harbison Projects</span></div>
    <div class="headline">
      <div class="big">DYNAMIC</div>
      <div class="mid">PROFESSIONALS</div>
      <div class="bar">With Deep Histories</div>
      <div class="small">OF MANAGING</div>
    </div>
    <div class="note">Significant Projects Inside Of The Restaurant,<br>Retail And Entertainment Space.</div>
    <div class="label">COMPETITIVE ADVANTAGE</div>
    <p>An intimate knowledge and proven track record of managing Design, Procurement, Architectural, and Construction efforts <b>simultaneously</b> to produce Undeniable Results</p>
    <p>“Our <b>Purpose</b> is to create High Level Experiences for our clients through Design, Planning, Construction and Development. ”</p>
    <p class="network">Extensive Network of Qualified Subcontractor Trades &amp; Vendors</p>
    <ul class="offer-list">
      <li>General Construction</li><li><span class="plus"></span></li>
      <li>Program Management</li><li><span class="plus"></span></li>
      <li>Design</li><li><span class="plus"></span></li>
      <li>Owner Rep</li>
    </ul>
  </div>

  <div class="abs services">
    <h2>SERVICES</h2>
    <ul>
      <li>Program Management<span class="dot"></span></li>
      <li>Pre-Construction /<br>Design Phase<span class="dot"></span></li>
      <li>Project &amp; Construction<br>Management<span class="dot"></span></li>
      <li>Scheduling<span class="dot"></span></li>
      <li>Owner Representation<span class="dot"></span></li>
    </ul>
  </div>

  <div class="abs contact">
    <div class="lead">Contact Us Now</div>
    <div class="phone"><svg viewBox="0 0 24 24"><path fill="#e5261f" d="M6.6 10.8a15 15 0 0 0 6.6 6.6l2.2-2.2a1 1 0 0 1 1-.25 11.4 11.4 0 0 0 3.6.57 1 1 0 0 1 1 1V20a1 1 0 0 1-1 1A17 17 0 0 1 3 4a1 1 0 0 1 1-1h3.5a1 1 0 0 1 1 1c0 1.25.2 2.45.57 3.57a1 1 0 0 1-.25 1z"/></svg>214-555-0193</div>
    <div class="web">www.<span>harbisonproj</span>group.example</div>
  </div>
  <div class="abs corner-name"><span class="square"></span>Harbison</div>
</section>

<section class="page page--back">
  <svg class="page-art" viewBox="0 0 530 685">
    <polygon points="0,0 530,0 530,55 265,95 0,55" fill="#161616"/>
    <polygon points="0,610 265,445 530,610 530,640 265,478 0,640" fill="#ececec"/>
    <polygon points="20,620 265,462 480,600 460,614 265,490 35,640" fill="#e5261f"/>
    <polygon points="40,685 40,650 265,498 470,632 470,685" fill="#161616"/>
    <polygon points="500,560 530,540 530,685 500,685" fill="#161616"/>
    <polygon points="347,327 423,371 423,459 347,503 271,459 271,371" fill="#e5261f"/>
    <g role="img" aria-label="Modern restaurant building with timber canopy under blue sky">
      <defs>
        <linearGradient id="canopy" x1="0" y1="0" x2="0" y2="1">
          <stop offset="0" stop-color="#7fb2d8"/><stop offset=".6" stop-color="#b08a64"/><stop offset="1" stop-color="#5f6b4a"/>
        </linearGradient>
        <linearGradient id="patio" x1="0" y1="0" x2="0" y2="1">
          <stop offset="0" stop-color="#23357a"/><stop offset=".6" stop-color="#a33a2a"/><stop offset="1" stop-color="#6a5a4a"/>
        </linearGradient>
      </defs>
      <polygon points="347,335 416,375 416,455 347,495 278,455 278,375" fill="url(#canopy)"/>
    </g>
    <polygon points="452,384 528,428 528,516 452,560 376,516 376,428" fill="#e5261f"/>
    <g role="img" aria-label="Restaurant patio with red sign letters at night">
      <polygon points="452,392 521,432 521,512 452,552 383,512 383,432" fill="url(#patio)"/>
    </g>
  </svg>

  <div class="abs why">
    <h1>WHY HARBISON BUILDING MANAGEMENT?</h1>
    <div class="simple">SIMPLE....</div>
  </div>

  <div class="abs divider"></div>

  <div class="abs reasons reasons--left">
    <div class="reason">
      <h3><span class="dot"></span>Cost Savings</h3>
      <p>If your concepts’ annual project volume is between (1 – 15) projects, you could save money outsourcing, vs utilizing in-house CM’s or PM’s.<br><b>a.</b><strong>Why?</strong> When you compare the compensation package w/ all benefits of a qualified Project Manager with 5+ year of management experience, the per-project cost burden from Harbison, is potentially 20-30 % less.</p>
    </div>
    <div class="reason">
      <h3><span class="dot"></span>Speed</h3>
      <p>Most likely, we are going to have much more robust processes and systems in place managing multiple projects simultaneously, at a more dynamic pace.<br><b>a.</b><strong>Benefit to You?</strong> Projects will move through the life cycle more quickly, efficiently and successfully, with guaranteed outcomes.</p>
    </div>
    <div class="reason">
      <h3><span class="dot"></span>Integrity</h3>
      <p>Because we are outsourced, we will push information faster, and communicate at a much higher level than an internal resource.<br><b>a.</b><strong>Why?</strong> Our value add, is your piece of mind and delivering results. We have a long term vision and strategy, and we are only as good as our last project. We have to keep delivering, while maintaining a high level experience to our customers so that we can thrive and grow.</p>
    </div>
  </div>

  <div class="abs reasons reasons--right">
    <div class="reason">
      <h3><span class="dot"></span>Technology</h3>
      <p>We utilize the latest project management software platforms to ensure high level collaboration, accountability and information transfer.<br><b>a.</b><strong>Scheduling</strong><br><b>b.</b><strong>Spreadsheets</strong></p>
    </div>
    <div class="reason">
      <h3><span class="dot"></span>Experience</h3>
      <p>Put simply, our team has managed hundreds of projects from restaurant, retail, commercial, warehouse, and government / military logistics – nationwide, and oversees.<br><b>a.</b><strong>What does this mean to you?</strong> You get the benefit of “best practices” we’ve acquired from partnering with other industry leading concepts and organizations.</p>
    </div>
  </div>

  <div class="abs back-name"><span class="square"></span>Harbison Projects</div>

  <div class="abs contact">
    <div class="lead">Contact Us Now</div>
    <div class="phone"><svg viewBox="0 0 24 24"><path fill="#e5261f" d="M6.6 10.8a15 15 0 0 0 6.6 6.6l2.2-2.2a1 1 0 0 1 1-.25 11.4 11.4 0 0 0 3.6.57 1 1 0 0 1 1 1V20a1 1 0 0 1-1 1A17 17 0 0 1 3 4a1 1 0 0 1 1-1h3.5a1 1 0 0 1 1 1c0 1.25.2 2.45.57 3.57a1 1 0 0 1-.25 1z"/></svg>214-555-0193</div>
    <div class="web">www.<span>harbisonproj</span>group.example</div>
  </div>
</section>

</body>
</html>
```